Lebel for 500g Honey Jar

We want a design for a 500g honey bottle or Jar as shown in the attached image . All Requirement has been put in the attached brief document .
Also Logo and images have been uploaded . Feel free to play arround with the selected solor schemes .

Target Market(s)

Retail Market

Industry/Entity Type

FMCG

Colors
00AB8E
00BBA5
67D7C9
C6EFE9
E9F9F6
59FF00
82FF00
B8FF75
E3FFCB
F4FFEA
FFC000
F8CF3A
FAE287
FDF2CF
FEFAEE
F0912C
F2A743
F7CA91
FBE8D2
FDF5EE
EE7325
F08F49
F5BC92
FAE3D3
FDF4ED

Requirements
Must have
• The desing must contain the company Address, Logo , and Nutritional Facts
Nice to have
• Image of a honey Bee , see samples attahed

```html
<!DOCTYPE html>
<html lang="en">
<head>
<meta charset="utf-8">
<title>Brightvale Pure Honey – 500 GM Label</title>
<link rel="stylesheet" href="https://fonts.googleapis.com/css2?family=Montserrat:wght@500;700;800&family=Yellowtail&display=swap">
<style>
  :root {
    --backdrop: #c3c3c3;
    --label-cream: #fefaee;
    --label-warm: #fdf2cf;
    --honey-orange: #ee7325;
    --honey-amber: #f0912c;
    --honey-gold: #ffc000;
    --honey-light: #fae287;
    --leaf-green: #7dbb2a;
    --ink: #1d1d1b;
    --white: #ffffff;
  }
  * { margin: 0; padding: 0; box-sizing: border-box; }
  html, body { width: 1200px; height: 1200px; overflow: hidden; }
  body {
    background: var(--backdrop);
    font-family: "Montserrat", sans-serif;
    position: relative;
  }
  .label {
    position: absolute;
    left: 380px; top: 200px;
    width: 440px; height: 800px;
    background: linear-gradient(180deg, var(--white) 0%, var(--label-cream) 45%, var(--label-warm) 100%);
    clip-path: polygon(20% 0, 80% 0, 100% 13%, 100% 87%, 80% 100%, 20% 100%, 0 87%, 0 13%);
    text-align: center;
  }
  .drip-band {
    position: absolute; left: 0; top: 0; width: 100%; height: 120px;
    background: linear-gradient(180deg, var(--honey-amber) 0%, var(--honey-gold) 60%, rgba(255,192,0,0) 100%);
  }
  .brand-name {
    position: absolute; left: 0; width: 100%; top: 148px;
    font-weight: 700; font-size: 60px; letter-spacing: -1px;
    color: var(--ink);
  }
  .product-pure {
    position: absolute; left: 0; width: 100%; top: 262px;
    font-weight: 500; font-size: 34px; color: var(--leaf-green);
    padding-left: 70px;
  }
  .product-honey {
    position: absolute; left: 0; width: 100%; top: 290px;
    font-family: "Yellowtail", cursive;
    font-size: 96px; line-height: 1; color: var(--honey-orange);
  }
  .claim-band {
    position: absolute; left: 85px; top: 412px;
    width: 270px; height: 34px;
    background: var(--leaf-green);
    color: var(--white);
    font-weight: 700; font-size: 17px; line-height: 34px;
    clip-path: polygon(3% 0, 100% 0, 97% 100%, 0 100%);
  }
  .badge-row {
    position: absolute; left: 70px; top: 466px; width: 300px;
    display: flex; justify-content: space-between; align-items: center;
  }
  .badge {
    width: 80px; height: 80px; border-radius: 50%;
    border: 3px solid var(--honey-orange);
    background: var(--white);
    display: flex; flex-direction: column; align-items: center; justify-content: center;
    color: var(--honey-orange);
    font-weight: 800; font-size: 7.5px; line-height: 1.15;
  }
  .badge svg { margin-top: 3px; }
  .badge-divider { width: 1px; height: 64px; border-left: 1px dashed #b7a98c; }
  .serving-art {
    position: absolute; left: 90px; top: 575px;
    width: 260px; height: 185px; border-radius: 50% 50% 46% 46%;
    background: radial-gradient(circle at 50% 55%, var(--honey-gold) 0%, var(--honey-amber) 45%, var(--honey-light) 75%, rgba(250,226,135,0) 100%);
  }
  .net-weight {
    position: absolute; left: 110px; bottom: 0;
    width: 220px; height: 38px;
    background: var(--honey-amber);
    color: var(--white);
    font-weight: 700; font-size: 17px; line-height: 36px;
    border-radius: 14px 14px 0 0;
  }
</style>
</head>
<body>
  <main class="label">
    <div class="drip-band" role="img" aria-label="Dripping honey border across the top of the label"></div>
    <div class="brand-name">brightvale</div>
    <div class="product-pure">Pure</div>
    <div class="product-honey">Honey</div>
    <div class="claim-band">100% PURE &amp; NATURAL</div>
    <div class="badge-row">
      <div class="badge">ZERO<br>PRESERVATIVE
        <svg width="22" height="22" viewBox="0 0 22 22"><circle cx="11" cy="11" r="9" fill="none" stroke="#ee7325" stroke-width="2"/><line x1="5" y1="17" x2="17" y2="5" stroke="#ee7325" stroke-width="2"/></svg>
      </div>
      <div class="badge-divider"></div>
      <div class="badge">ZERO<br>ADDITIVE
        <svg width="22" height="22" viewBox="0 0 22 22"><circle cx="11" cy="11" r="9" fill="none" stroke="#ee7325" stroke-width="2"/><line x1="5" y1="17" x2="17" y2="5" stroke="#ee7325" stroke-width="2"/></svg>
      </div>
      <div class="badge-divider"></div>
      <div class="badge">ZERO<br>COLOURING
        <svg width="22" height="22" viewBox="0 0 22 22"><circle cx="11" cy="11" r="9" fill="none" stroke="#ee7325" stroke-width="2"/><line x1="5" y1="17" x2="17" y2="5" stroke="#ee7325" stroke-width="2"/></svg>
      </div>
    </div>
    <div class="serving-art" role="img" aria-label="Bowl of golden honey with a wooden dipper, honeycomb, flowers and bees"></div>
    <div class="net-weight">500 GM</div>
  </main>
</body>
</html>
```